Create Business cards for Pet business

Original Business card creation
Please be original. If I wanted a generic business card template, I would have made one myself
Please use colour scheme

Adobe Files like PSD and AI are required
Name : Mark Lane
Website : [login to view URL]
Phone number :0491736258

```html
<!DOCTYPE html>
<html lang="en">
<head>
<meta charset="UTF-8">
<title>Pawnest Business Cards</title>
<link rel="stylesheet" href="https://fonts.googleapis.com/css2?family=Montserrat:wght@400;500;700&display=swap">
<style>
  :root {
    --stage: #3a3b3e;
    --brand-blue: #1a76c0;
    --brand-blue-soft: #2b86cd;
    --brand-orange: #f59a1e;
    --card-white: #ffffff;
    --ink: #3c3c3c;
  }
  * { box-sizing: border-box; margin: 0; padding: 0; }
  html, body {
    width: 1200px; height: 900px; overflow: hidden;
    background: var(--stage);
    font-family: "Montserrat", sans-serif;
  }
  .card {
    position: absolute;
    width: 700px; height: 400px;
    border-radius: 26px;
    overflow: hidden;
    box-shadow: 0 12px 30px rgba(0,0,0,0.35);
  }
  /* Front card */
  .card-front {
    left: 90px; top: 60px;
    background: var(--brand-blue);
  }
  .front-border-pattern {
    position: absolute; inset: 18px;
    border: 34px solid var(--brand-blue-soft);
    border-radius: 14px;
  }
  .front-brand {
    position: absolute; left: 0; right: 0; top: 170px;
    text-align: center;
    font-weight: 700; font-size: 64px;
    color: var(--card-white);
    letter-spacing: 1px;
  }
  /* Back card */
  .card-back {
    left: 410px; top: 470px;
    background: var(--card-white);
  }
  .back-band {
    position: absolute; left: 150px; top: 0;
    width: 52px; height: 400px;
    background: linear-gradient(to bottom,
      var(--brand-orange) 0, var(--brand-orange) 70px,
      var(--brand-blue) 70px, var(--brand-blue) 330px,
      var(--brand-orange) 330px, var(--brand-orange) 400px);
  }
  .back-info {
    position: absolute; right: 40px; top: 30px;
    text-align: right;
  }
  .back-brand {
    font-weight: 700; font-size: 52px;
    color: var(--brand-blue);
    line-height: 1.1;
  }
  .person-name {
    margin-top: 26px;
    font-weight: 700; font-size: 32px;
    color: var(--brand-blue);
    letter-spacing: 1px;
  }
  .person-name .surname { color: var(--brand-orange); }
  .person-role {
    font-weight: 500; font-size: 17px;
    color: var(--ink);
    letter-spacing: 5px;
    margin-right: 36px;
  }
  .contact-list {
    list-style: none;
    margin-top: 14px;
  }
  .contact-item {
    display: flex; justify-content: flex-end; align-items: center;
    gap: 14px;
    font-size: 18px; color: var(--ink);
    letter-spacing: 1px;
    height: 34px;
  }
  .contact-icon {
    width: 22px; height: 22px;
    flex: none;
  }
</style>
</head>
<body>

<section class="card card-front">
  <div class="front-border-pattern" role="img" aria-label="Border of small paw print motifs"></div>
  <div class="front-brand">Pawnest</div>
</section>

<section class="card card-back">
  <div class="back-band"></div>
  <div class="back-info">
    <div class="back-brand">Pawnest</div>
    <div class="person-name">MARK <span class="surname">LANE</span></div>
    <div class="person-role">DIRECTOR</div>
    <ul class="contact-list">
      <li class="contact-item">
        <span>0491736258</span>
        <svg class="contact-icon" viewBox="0 0 24 24" aria-hidden="true">
          <circle cx="12" cy="12" r="12" fill="var(--brand-blue)"/>
          <path d="M8.5 6.5l2 2.2-1.2 1.6c.8 1.7 2 2.9 3.6 3.7l1.6-1.2 2.2 2-1.2 2c-4.8-.5-8.2-3.9-8.6-8.6z" fill="#fff"/>
        </svg>
      </li>
      <li class="contact-item">
        <span>mark@pawnest.com</span>
        <svg class="contact-icon" viewBox="0 0 24 24" aria-hidden="true">
          <circle cx="12" cy="12" r="12" fill="var(--brand-blue)"/>
          <rect x="6" y="8" width="12" height="8.5" rx="1" fill="#fff"/>
          <path d="M6.5 8.5l5.5 4.2 5.5-4.2" fill="none" stroke="var(--brand-blue)" stroke-width="1.3"/>
        </svg>
      </li>
      <li class="contact-item">
        <span>www.pawnest.com</span>
        <svg class="contact-icon" viewBox="0 0 24 24" aria-hidden="true">
          <circle cx="12" cy="12" r="12" fill="var(--brand-blue)"/>
          <g fill="none" stroke="#fff" stroke-width="1.3">
            <circle cx="12" cy="12" r="6"/>
            <ellipse cx="12" cy="12" rx="2.6" ry="6"/>
            <line x1="6" y1="12" x2="18" y2="12"/>
          </g>
        </svg>
      </li>
    </ul>
  </div>
</section>

</body>
</html>
```